Kestrel Roadway Wheels

I need a wrap designed for a box truck. The company is a mobile tire shop. It’s a tire shop on wheels, that comes anywhere you are to service your tires.

```html
<!DOCTYPE html>
<html lang="en">
<head>
<meta charset="UTF-8">
<title>Kestrel Roadway Wheels – Box Truck Wrap</title>
<link rel="stylesheet" href="https://fonts.googleapis.com/css2?family=Exo+2:wght@600;700&family=Russo+One&display=swap">
<style>
  :root {
    --navy-deep: #1c2138;
    --navy: #2a3150;
    --navy-light: #353d5e;
    --sky: #3a9ae0;
    --band-blue: #2f6fc0;
    --band-blue-light: #3f8fd8;
    --white: #f4f5f7;
    --denim: #2d6fb5;
    --denim-dark: #1d4f8a;
  }
  * { margin: 0; padding: 0; box-sizing: border-box; }
  html, body { width: 1200px; height: 680px; overflow: hidden; background: #ffffff; }
  .wrap-panel {
    position: relative;
    width: 1200px;
    height: 680px;
    overflow: hidden;
    background: radial-gradient(ellipse at 40% 45%, var(--navy-light) 0%, var(--navy) 45%, var(--navy-deep) 100%);
    font-family: "Exo 2", Arial, sans-serif;
  }
  .tagline {
    position: absolute;
    left: 26px;
    top: 26px;
    font-size: 31px;
    font-weight: 700;
    color: var(--sky);
    letter-spacing: 0.2px;
    white-space: nowrap;
  }
  .service-photo {
    position: absolute;
    left: 760px;
    top: 80px;
    width: 440px;
    height: 600px;
    background: linear-gradient(100deg, #1a1e2c 0%, #2b3145 38%, var(--denim-dark) 62%, var(--denim) 100%);
  }
  .brand {
    position: absolute;
    left: 50px;
    top: 100px;
    display: flex;
    align-items: center;
    gap: 22px;
  }
  .brand-dot {
    width: 110px;
    height: 110px;
    border-radius: 50%;
    background: var(--sky);
    flex: none;
  }
  .brand-name {
    font-size: 72px;
    line-height: 0.98;
    font-weight: 700;
    color: var(--white);
  }
  .phone-band {
    position: absolute;
    left: 0;
    top: 333px;
    width: 720px;
    height: 80px;
    background: linear-gradient(90deg, var(--band-blue) 0%, var(--band-blue-light) 70%, rgba(63,143,216,0) 100%);
  }
  .phone-number {
    position: absolute;
    left: 46px;
    top: 336px;
    font-size: 70px;
    font-weight: 700;
    color: var(--white);
    letter-spacing: 1px;
    line-height: 74px;
  }
  .service-list {
    position: absolute;
    left: 26px;
    top: 452px;
    list-style: none;
  }
  .service-list li {
    display: flex;
    align-items: center;
    gap: 8px;
    height: 43px;
    font-size: 27px;
    font-weight: 600;
    color: var(--white);
    white-space: nowrap;
  }
  .service-list .tick { width: 26px; height: 26px; flex: none; }
  .service-list .extra { margin-left: 40px; }
  .promise {
    position: absolute;
    left: 680px;
    top: 598px;
    width: 270px;
    text-align: center;
    font-family: "Russo One", Arial, sans-serif;
    font-style: italic;
    font-size: 38px;
    line-height: 40px;
    color: var(--sky);
  }
</style>
</head>
<body>
<main class="wrap-panel">
  <p class="tagline">DON’T WAIT AT A TIRE SHOP, WHEEL COME TO YOU</p>

  <div class="service-photo" role="img" aria-label="Technician in blue work overalls and grey gloves rolling a tire"></div>

  <div class="brand">
    <span class="brand-dot"></span>
    <h1 class="brand-name">Kestrel Roadway<br>Wheels</h1>
  </div>

  <div class="phone-band"></div>
  <p class="phone-number">843-555-0142</p>

  <ul class="service-list">
    <li><svg class="tick" viewBox="0 0 26 26"><circle cx="12" cy="14" r="9" fill="none" stroke="#3a9ae0" stroke-width="3"/><path d="M7 13l5 5 12-14" fill="none" stroke="#3a9ae0" stroke-width="3.5" stroke-linecap="round"/></svg>TIRE MOUNTING &amp; INSTALLATION</li>
    <li><svg class="tick" viewBox="0 0 26 26"><circle cx="12" cy="14" r="9" fill="none" stroke="#3a9ae0" stroke-width="3"/><path d="M7 13l5 5 12-14" fill="none" stroke="#3a9ae0" stroke-width="3.5" stroke-linecap="round"/></svg>NEW &amp; USED TIRES<span class="extra">TIRE REPAIRS</span></li>
    <li><svg class="tick" viewBox="0 0 26 26"><circle cx="12" cy="14" r="9" fill="none" stroke="#3a9ae0" stroke-width="3"/><path d="M7 13l5 5 12-14" fill="none" stroke="#3a9ae0" stroke-width="3.5" stroke-linecap="round"/></svg>COMPETITIVE WHOLESALE PRICING</li>
    <li><svg class="tick" viewBox="0 0 26 26"><circle cx="12" cy="14" r="9" fill="none" stroke="#3a9ae0" stroke-width="3"/><path d="M7 13l5 5 12-14" fill="none" stroke="#3a9ae0" stroke-width="3.5" stroke-linecap="round"/></svg>EMERGENCY ROADSIDE SERVICE</li>
    <li><svg class="tick" viewBox="0 0 26 26"><circle cx="12" cy="14" r="9" fill="none" stroke="#3a9ae0" stroke-width="3"/><path d="M7 13l5 5 12-14" fill="none" stroke="#3a9ae0" stroke-width="3.5" stroke-linecap="round"/></svg>LOW PROFILE TIRES</li>
  </ul>

  <p class="promise">We Come<br>To You</p>
</main>
</body>
</html>
```